Religious Church Business Card Design

We need a business card design for our new pastor. We would like something warm and inviting. colors grape and white.
Updates

Church # 718-555-0139 and Cell # 718-555-0172

I also have a logo i tried to upload

Industry/Entity Type

Business

Contact Information for Business Card

Elder Ray Whitlock, Cedar Hollow Fellowship Church, 4172 Larkmoor Avenue, Bronx, NY 10982, email: raywhitlock@cedarhollowfellowship.example, www.cedarhollowfellowship.example

Colors
886aae

```html
<!DOCTYPE html>
<html lang="en">
<head>
<meta charset="utf-8">
<title>Elder Ray Whitlock – Business Card</title>
<link href="https://fonts.googleapis.com/css2?family=Questrial&display=swap" rel="stylesheet">
<style>
  :root {
    --grape: #7b5cff;
    --paper: #ffffff;
    --ink: #7458f5;
  }
  * { margin: 0; padding: 0; box-sizing: border-box; }
  html, body { width: 1200px; height: 702px; overflow: hidden; background: var(--paper); }
  .card {
    position: relative;
    width: 1200px;
    height: 702px;
    background: var(--paper);
    font-family: "Questrial", "Helvetica Neue", Arial, sans-serif;
  }
  .header-band {
    position: absolute;
    left: 0; top: 0;
    width: 1200px; height: 380px;
    background: var(--grape);
  }
  .brand-mark {
    position: absolute;
    left: 70px; top: 70px;
    width: 270px;
    display: flex;
    flex-direction: column;
    align-items: center;
    color: var(--paper);
  }
  .brand-mark .ring {
    width: 130px; height: 130px;
    border: 4px solid var(--paper);
    border-radius: 50%;
    margin-bottom: 22px;
  }
  .brand-mark .brand-name {
    font-size: 26px;
    line-height: 1.25;
    text-align: center;
    letter-spacing: 1px;
  }
  .pastor-name {
    position: absolute;
    left: 380px; top: 124px;
    font-size: 64px;
    font-weight: 400;
    letter-spacing: 3px;
    color: var(--paper);
    white-space: nowrap;
  }
  .church-name {
    position: absolute;
    left: 396px; top: 202px;
    font-size: 41px;
    letter-spacing: 2px;
    color: var(--paper);
    white-space: nowrap;
  }
  .contact {
    position: absolute;
    left: 0; width: 1200px;
    color: var(--ink);
    white-space: nowrap;
    letter-spacing: 1px;
  }
  .contact.phones { top: 528px; font-size: 29px; padding-left: 220px; letter-spacing: 1.5px; }
  .contact.phones .gap { display: inline-block; width: 22px; }
  .contact.address { top: 575px; font-size: 25px; padding-left: 340px; }
  .contact.online { top: 612px; font-size: 23px; text-align: center; }
</style>
</head>
<body>
  <div class="card">
    <div class="header-band"></div>

    <div class="brand-mark">
      <div class="ring"></div>
      <div class="brand-name">Cedar Hollow<br>Fellowship Church</div>
    </div>

    <h1 class="pastor-name">Elder Ray Whitlock</h1>
    <h2 class="church-name">Cedar Hollow Fellowship Church</h2>

    <p class="contact phones">Church 718-555-0139<span class="gap"></span>Cell&nbsp; 718-555-0172</p>
    <p class="contact address">4172 Larkmoor Avenue, Bronx, NY 10982,</p>
    <p class="contact online">email: raywhitlock@cedarhollowfellowship.example, www.cedarhollowfellowship.example</p>
  </div>
</body>
</html>
```